Marlow Cellar Holdings LLC Website

We need a website design for a winery. Our consumer target market will be a millennial demographic, hip, fresh, and upscale.
High end impact images, interactive pages, e-commerce, etc...
The following are examples of what we would be looking to accomplish:

http://www.perchhillestate.example/
ostrowell.example
http://www.kestrelpitchstudio.example/portfolio/

There is no tasting room, all sales are via wine club and internet sales.

Target Market(s)

Millennials are the generation born between 1982 and sometime in the early 2000’s. However, these boundaries aren’t set in stone. Usually highly educated professionals with disposable income.

```html
<!DOCTYPE html>
<html lang="en">
<head>
<meta charset="utf-8">
<title>Marlow Cellar Group</title>
<link href="https://fonts.googleapis.com/css2?family=Cormorant+Garamond:wght@400;500;600&family=Great+Vibes&family=Open+Sans:wght@400;600&display=swap" rel="stylesheet">
<style>
:root{
  --gold:#c19a3a;
  --red:#c8151e;
  --ink:#1b1b1b;
  --text:#333;
  --white:#fff;
  --footer:#2a2a2d;
  --footer-deep:#1f1f21;
  --muted:#9a9a9a;
  --serif:"Cormorant Garamond", Georgia, serif;
  --script:"Great Vibes", cursive;
  --sans:"Open Sans", Arial, sans-serif;
}
*{box-sizing:border-box;margin:0;padding:0}
html,body{width:1200px;height:3696px;overflow:hidden;background:#fff}
body{position:relative;font-family:var(--sans);color:var(--text)}
section,header,footer{position:absolute;left:0;width:1200px}
.abs{position:absolute}
.photo{position:absolute}
.btn{position:absolute;display:flex;align-items:center;justify-content:center;font-family:var(--serif);font-size:15px;letter-spacing:2px;text-transform:uppercase;height:42px;width:150px}
.btn-gold{background:var(--gold);color:#fff}
.btn-outline{border:1.5px solid #fff;color:#fff}
.script{font-family:var(--script);font-weight:400;white-space:nowrap}
.caps{font-family:var(--serif);text-transform:uppercase;font-weight:400;white-space:nowrap}
.body-copy{font-size:12.5px;line-height:25px}

/* hero */
.hero{top:0;height:609px}
.hero .photo{inset:0;background:radial-gradient(ellipse at 70% 40%,#4c4a4a 0%,#2c2a2b 45%,#161516 100%)}
.hero .shade{position:absolute;inset:0;background:linear-gradient(180deg,rgba(0,0,0,.35),rgba(0,0,0,.15) 50%,rgba(0,0,0,.35))}
.brand{left:70px;top:40px;width:180px;height:105px;display:flex;align-items:center;gap:10px}
.brand-mark{width:14px;height:14px;background:var(--gold)}
.brand-name{font-family:var(--serif);font-weight:600;color:var(--gold);font-size:30px;line-height:32px}
.main-nav{left:310px;top:68px;display:flex;gap:47px;font-size:12px;letter-spacing:.5px;color:#fff;text-transform:uppercase}
.nav-icons{left:1055px;top:64px;display:flex;gap:28px;align-items:center}
.hero-title{top:195px;width:1200px;text-align:center;color:#fff}
.hero-title .script{font-size:96px;line-height:104px}
.hero-title .caps{color:var(--gold);font-size:78px;line-height:84px;letter-spacing:2px}
.hero-sub{top:400px;width:1200px;text-align:center;color:#fff;font-family:var(--serif);font-size:27px;line-height:40px;text-transform:uppercase}
.slide-dots{left:1159px;top:285px;display:flex;flex-direction:column;gap:16px}
.slide-dots span{width:8px;height:8px;border-radius:50%;background:rgba(255,255,255,.45)}
.scroll-down{left:573px;top:582px;width:54px;height:54px;border-radius:50%;background:#fff}

/* welcome */
.welcome{top:609px;height:359px;text-align:center}
.welcome .caps{position:absolute;top:66px;width:100%;font-size:38px;line-height:44px;color:var(--ink);letter-spacing:1px}
.welcome .script{position:absolute;top:108px;width:100%;font-size:62px;line-height:72px;color:var(--ink)}
.welcome .body-copy{position:absolute;left:200px;top:203px;width:800px;color:#555}

/* wine club */
.club{top:968px;height:505px}
.club .photo{inset:0;background:linear-gradient(90deg,#2a1409 0%,#5a2f16 35%,#7a4422 60%,#3d1d0e 100%)}
.club h2{left:99px;top:133px;font-size:56px;line-height:60px;color:#fff;letter-spacing:1px}
.club .body-copy{left:99px;top:208px;width:560px;color:#fff}
.club .btn{left:99px;top:333px}

/* about */
.about{top:1473px;height:464px}
.about .photo{left:0;top:0;width:599px;height:464px;background:linear-gradient(120deg,#3a2a1e,#6b5443 45%,#2a231f)}
.about .panel{position:absolute;left:599px;top:0;width:601px;height:464px;background:var(--red)}
.about h2{left:707px;top:84px;font-size:36px;line-height:42px;color:#fff;letter-spacing:1px}
.about .script{left:707px;top:128px;font-size:52px;line-height:62px;color:#fff}
.about .body-copy{left:710px;top:208px;width:430px;color:#fff}
.about .btn{left:712px;top:334px}

/* products */
.products{top:1937px;height:884px;text-align:center}
.products .caps{position:absolute;top:70px;width:100%;font-size:38px;line-height:44px;color:var(--ink)}
.products .heading-script{position:absolute;top:114px;width:100%;font-size:62px;line-height:72px;color:var(--ink)}
.product{position:absolute;top:230px;width:300px;text-align:center}
.product .bottle{margin:0 auto;width:72px;height:322px;border-radius:22px 22px 6px 6px}
.product h3{margin-top:38px;font-family:var(--serif);font-weight:500;font-size:21px;line-height:26px;color:var(--ink);text-transform:uppercase;letter-spacing:.5px}
.product p{margin-top:8px;font-size:12px;line-height:24px;color:#555}
.product .buy{margin-top:20px;display:flex;justify-content:center;align-items:center;gap:26px}
.price{font-family:var(--serif);font-size:29px;color:var(--ink)}
.buy-btn{background:var(--gold);color:#fff;font-family:var(--serif);font-size:14px;letter-spacing:2px;width:120px;height:40px;display:flex;align-items:center;justify-content:center}
.arrow{position:absolute;top:371px;width:40px;height:40px;border-radius:50%;border:1.5px solid #bbb}
.pager{position:absolute;top:815px;left:570px;display:flex;gap:7px}
.pager span{width:8px;height:8px;border-radius:50%;background:#ccc}
.pager span.on{background:var(--red)}

/* shop */
.shop{top:2821px;height:505px}
.shop .photo{inset:0;background:linear-gradient(90deg,#4a1e10 0%,#8a4a1c 30%,#c9853a 55%,#8a4a1c 80%,#4a2410 100%)}
.shop h2{left:562px;top:98px;font-size:56px;line-height:60px;color:#fff;letter-spacing:1px}
.shop .script{left:562px;top:158px;font-size:52px;line-height:62px;color:#fff}
.shop .body-copy{left:562px;top:235px;width:560px;color:#fff}
.shop .btn{left:562px;top:358px}

/* footer */
.site-footer{top:3326px;height:316px;background:var(--footer);color:var(--muted)}
.footer-brand{left:99px;top:34px;display:flex;align-items:center;gap:8px}
.footer-brand .brand-name{font-size:22px;line-height:24px}
.footer-col{position:absolute;top:125px}
.footer-col h4{font-family:var(--serif);font-weight:600;font-size:14px;color:#fff;text-transform:uppercase;letter-spacing:1px;margin-bottom:12px}
.footer-col li{list-style:none;font-size:11.5px;line-height:24px;white-space:nowrap}
.contact-line{display:flex;align-items:center;gap:8px}
.social{position:absolute;top:44px;display:flex;align-items:center;gap:14px;font-size:11px;line-height:15px}
.social .sq{width:40px;height:40px}
.stay h4{font-size:20px;font-weight:500;letter-spacing:1px}
.stay p{font-size:11px;line-height:18px;width:340px}
.signup{display:flex;gap:10px;margin-top:18px}
.signup .field{width:234px;height:37px;background:#1c1c1e;font-size:11px;color:#888;display:flex;align-items:center;padding-left:14px}
.signup .go{width:94px;height:37px;background:var(--gold);color:#fff;font-family:var(--serif);font-size:14px;letter-spacing:1.5px;display:flex;align-items:center;justify-content:center}
.copyright{top:3642px;height:54px;background:var(--footer-deep);color:#8a8a8a;font-size:11px;display:flex;align-items:center;justify-content:center}
</style>
</head>
<body>

<header class="hero">
  <div class="photo" role="img" aria-label="Photo of a hand lifting a wine bottle from a softly lit cellar"></div>
  <div class="shade"></div>
  <div class="abs brand"><span class="brand-mark"></span><span class="brand-name">Marlow<br>Cellar</span></div>
  <nav class="abs main-nav"><span>About Us</span><span>Our Wines</span><span>Online Store</span><span>Wine Club</span><span>News &amp; Events</span><span>Contact</span></nav>
  <div class="abs nav-icons">
    <svg width="22" height="24" viewBox="0 0 22 24" fill="none" stroke="#fff" stroke-width="1.6"><path d="M3 8h16l-1 14H4z"/><path d="M7 8V5a4 4 0 0 1 8 0v3"/></svg>
    <svg width="28" height="20" viewBox="0 0 28 20" stroke="#fff" stroke-width="1.6"><path d="M0 2h28M0 10h28M0 18h28"/></svg>
  </div>
  <div class="abs hero-title">
    <div class="script">Marlow</div>
    <div class="caps">Cellar Group</div>
  </div>
  <p class="abs hero-sub">Lorem ipsum is simply dummy text of the printing and<br>typesetting industry</p>
  <div class="abs slide-dots"><span></span><span></span><span></span><span></span></div>
  <div class="abs scroll-down">
    <svg width="54" height="54" viewBox="0 0 54 54" fill="none" stroke="#555" stroke-width="1.6"><path d="M20 20l7 6 7-6M20 27l7 6 7-6"/></svg>
  </div>
</header>

<section class="welcome">
  <h2 class="caps">Welcome to</h2>
  <div class="script">Marlow Cellar Group</div>
  <p class="body-copy">Lorem Ipsum is simply dummy text of the printing and typesetting industry. Lorem Ipsum has been the industry's standard dummy text ever since the 1500s, when an unknown printer took a galley of type and scrambled it to make a type specimen book. It has survived not only five centuries, but also the leap into electronic typesetting, remaining essentially unchanged...</p>
</section>

<section class="club">
  <div class="photo" role="img" aria-label="Photo of red wine being poured into a glass against dark wood"></div>
  <h2 class="abs caps">Wine Club</h2>
  <p class="abs body-copy">Lorem Ipsum is simply dummy text of the printing and typesetting industry. Lorem Ipsum has been the industry's standard dummy text ever since the 1500s, when an unknown printer took a galley of type and scrambled it to make a type specimen book. It has survived not only five centuries, but also the leap into electronic typesetting, remaining essentially unchanged...</p>
  <a class="btn btn-gold">Click Here</a>
</section>

<section class="about">
  <div class="photo" role="img" aria-label="Photo of a man tasting red wine in a cellar"></div>
  <div class="panel"></div>
  <h2 class="abs caps">About</h2>
  <div class="abs script">Marlow Cellar Group</div>
  <p class="abs body-copy">Lorem Ipsum is simply dummy text of the printing and typesetting industry. Lorem Ipsum has been the industry's standard dummy text ever since the 1500s, when an unknown printer took a galley of type and scrambled it to make a type specimen book...</p>
  <a class="btn btn-outline">Click Here</a>
</section>

<section class="products">
  <h2 class="caps">Products of</h2>
  <div class="heading-script script">Marlow Cellar Group</div>
  <div class="arrow" style="left:59px"><svg width="40" height="40" viewBox="0 0 40 40" fill="none" stroke="#999" stroke-width="1.5"><path d="M23 14l-6 6 6 6"/></svg></div>
  <div class="arrow" style="left:1086px"><svg width="40" height="40" viewBox="0 0 40 40" fill="none" stroke="#999" stroke-width="1.5"><path d="M17 14l6 6-6 6"/></svg></div>

  <article class="product" style="left:87px">
    <div class="bottle" role="img" aria-label="Photo of a dark red wine bottle" style="background:linear-gradient(90deg,#120808,#3a1414 45%,#120808)"></div>
    <h3>2015 Rosé of Pinot Noir</h3>
    <p>Lorem Ipsum is simply dummy text of the printing and typesetting industry. Lorem Ipsum has been the industry's standard dummy</p>
    <div class="buy"><span class="price">$120.00</span><span class="buy-btn">BUY NOW</span></div>
  </article>
  <article class="product" style="left:449px">
    <div class="bottle" role="img" aria-label="Photo of a bright red wine bottle" style="background:linear-gradient(90deg,#5a0c10,#b8242c 45%,#5a0c10)"></div>
    <h3>2015 Rosé of Pinot Noir</h3>
    <p>Lorem Ipsum is simply dummy text of the printing and typesetting industry. Lorem Ipsum has been the industry's standard dummy</p>
    <div class="buy"><span class="price">$120.00</span><span class="buy-btn">BUY NOW</span></div>
  </article>
  <article class="product" style="left:811px">
    <div class="bottle" role="img" aria-label="Photo of a green white-wine bottle" style="background:linear-gradient(90deg,#3c3a10,#8a8a2c 45%,#3c3a10)"></div>
    <h3>2015 Rosé of Pinot Noir</h3>
    <p>Lorem Ipsum is simply dummy text of the printing and typesetting industry. Lorem Ipsum has been the industry's standard dummy</p>
    <div class="buy"><span class="price">$120.00</span><span class="buy-btn">BUY NOW</span></div>
  </article>
  <div class="pager"><span class="on"></span><span></span><span></span><span></span></div>
</section>

<section class="shop">
  <div class="photo" role="img" aria-label="Photo of grape clusters on the vine in warm sunset light"></div>
  <h2 class="abs caps">Shop</h2>
  <div class="abs script">Our Online Store</div>
  <p class="abs body-copy">Lorem Ipsum is simply dummy text of the printing and typesetting industry. Lorem Ipsum has been the industry's standard dummy text ever since the 1500s, when an unknown printer took a galley of type and scrambled it to make a type specimen book. It has survived not only five centuries, but also the leap into electronic typesetting, remaining essentially unchanged...</p>
  <a class="btn btn-gold">Buy Now</a>
</section>

<footer class="site-footer">
  <div class="abs footer-brand"><span class="brand-mark"></span><span class="brand-name">Marlow<br>Cellar</span></div>
  <div class="footer-col" style="left:108px">
    <h4>Welcome</h4>
    <ul><li>About Us</li><li>Our Wines</li><li>Online Store</li><li>Wine Club</li><li>News &amp; Events</li><li>Contact</li></ul>
  </div>
  <div class="footer-col" style="left:271px">
    <h4>Information</h4>
    <ul><li>Disclaimer</li><li>Privacy Policy</li><li>Terms of Conditions</li><li>Sitemap</li></ul>
  </div>
  <div class="footer-col" style="left:483px">
    <h4>Contact Info</h4>
    <ul>
      <li>120 Street name, City name,</li>
      <li>Country name : 000000</li>
      <li class="contact-line"><svg width="10" height="10" viewBox="0 0 10 10"><path d="M2 1l2 2-1 1.5 2.5 2.5L7 6l2 2-1.5 1.5C4 9 1 6 .5 2.5z" fill="#c19a3a"/></svg>Phone : + 5550 | 142 307</li>
      <li class="contact-line"><svg width="11" height="9" viewBox="0 0 11 9"><rect x=".5" y=".5" width="10" height="8" fill="none" stroke="#c19a3a"/><path d="M.5 .5l5 4 5-4" fill="none" stroke="#c19a3a"/></svg>Email : info@marlowcellar.example</li>
    </ul>
  </div>
  <div class="social" style="left:751px"><span class="sq" style="background:#2d4f9a"></span><span>Like us<br>on social page</span></div>
  <div class="social" style="left:926px"><span class="sq" style="background:#e0642a"></span><span>Subscribe<br>to news feeds</span></div>
  <div class="footer-col stay" style="left:751px;top:136px">
    <h4>Stay Connected</h4>
    <p>Subscribe to Our Newsletter to get Important News, Amazing Offers &amp; Inside Scoops:</p>
    <div class="signup"><span class="field">Enter your email id</span><span class="go">SIGNUP</span></div>
  </div>
</footer>
<div class="abs copyright" style="width:1200px">Copyright © 2016. Marlow Cellar Group. All rights reserved.</div>

</body>
</html>
```